I LOVE BRAMBLE CREST

I would like a one page site that links to my real estate team website. Bramble Crest is a upscale and diverse subdivision in Bethesda Maryland about 30 minutes from downtown DC.
I am thinking of a modern Mayberry w/ a global-hip look.
We have T-Ball, Soccer, bike trails, bunnies, dogs and cats, bee-keepers, farmer markets, GREAT PUBLIC SCHOOLS
kids, kids, kids
I live in this area and love it and want to sell more houses here so I want this webpage to link to my site but be unique to this subdivision.

Target Market(s)

real estate - home sellers and home buyers

Industry/Entity Type

Real Estate Agent

Coding

Coded - Design and coding required

Number of Pages Required

1 page

Font styles to use
Sans Serif

Requirements
Must have
• Clear message The Orson & Mirela Team sells in Bramble Crest
Nice to have
• Images that reflect the fantastic Modern Mayberry meet hip Global world feel

```html
<!DOCTYPE html>
<html lang="en">
<head>
<meta charset="utf-8">
<title>I Love Bramble Crest</title>
<link href="https://fonts.googleapis.com/css2?family=Raleway:wght@500;600;700;800&family=Open+Sans:wght@400;600;700&display=swap" rel="stylesheet">
<style>
:root{
  --blue:#3d9be0;
  --orange:#f2b12e;
  --ink:#1f2226;
  --text:#55595e;
  --muted:#8d9196;
  --line:#e3e4e6;
  --panel:#f3f4f5;
  --footer:#25272c;
  --footer-text:#c9cbcf;
}
*{box-sizing:border-box;margin:0;padding:0}
html,body{width:1200px;height:2748px;overflow:hidden;background:#fff}
body{font-family:"Open Sans",Arial,sans-serif;color:var(--text)}
.page{position:relative;width:1200px;height:2748px;overflow:hidden}
.abs{position:absolute}
.heading{font-family:"Raleway",Arial,sans-serif;font-weight:700;color:var(--ink);text-transform:uppercase}

/* header */
.top-rule{top:0;left:0;width:1200px;height:5px;background:var(--blue)}
.brand{left:99px;top:26px;font-family:"Raleway",Arial,sans-serif;font-weight:800;font-size:23px;color:var(--ink)}
.utility{right:99px;top:20px;font-size:12px;color:var(--text)}
.utility span{margin:0 6px}
.nav{right:99px;top:51px;display:flex;gap:33px;align-items:center;font-family:"Raleway",Arial,sans-serif;font-weight:700;font-size:13.5px;color:var(--ink)}
.nav .active{color:var(--orange)}

/* hero */
.hero{top:80px;left:0;width:1200px;height:411px;background:linear-gradient(180deg,#7f93aa 0%,#9aa7b3 35%,#6e6159 70%,#4a4a4e 100%)}
.hero-shade{top:80px;left:0;width:1200px;height:411px;background:rgba(20,30,50,.25)}
.hero-title{top:186px;width:1200px;text-align:center;font-family:"Raleway",Arial,sans-serif;font-weight:800;font-size:51px;color:#fff}
.hero-lead{top:258px;left:225px;width:750px;text-align:center;font-size:16.5px;line-height:28px;color:#fff;font-weight:600}
.hero-btn{top:330px;left:485px;width:230px;height:44px;border:2px solid #fff;background:var(--orange);color:#fff;font-family:"Raleway",Arial,sans-serif;font-weight:700;font-size:15px;display:flex;align-items:center;justify-content:center}
.hero-dots{top:445px;left:538px;display:flex;gap:6px}
.hero-dots i{display:block;width:26px;height:5px;background:#fff;border-radius:3px}
.hero-dots i:first-child{background:var(--blue)}

/* articles */
.section-title{left:99px;top:536px;font-size:20px}
.section-rule{left:99px;top:575px;width:587px;height:1px;background:var(--line)}
.article{left:99px;width:587px;height:354px}
.article-title{font-family:"Raleway",Arial,sans-serif;font-weight:700;font-size:15px;color:var(--ink);text-transform:uppercase}
.meta{position:absolute;top:31px;left:0;font-size:12px;color:var(--muted);display:flex;align-items:center;gap:6px}
.meta svg{width:11px;height:11px}
.meta .sep{margin:0 6px}
.progress{position:absolute;top:62px;left:0;width:587px;height:13px;background:var(--blue);border-radius:3px}
.progress-marker{position:absolute;top:54px;left:285px;width:16px;height:18px}
.thumb{position:absolute;top:108px;left:2px;width:253px;height:178px;border:3px solid #fff;box-shadow:0 0 0 1px #d9dadc}
.excerpt{position:absolute;top:106px;left:278px;width:309px;font-size:13px;line-height:23px;color:var(--text)}
.read-more{position:absolute;top:220px;left:278px;font-family:"Raleway",Arial,sans-serif;font-weight:700;font-size:12.5px;color:var(--orange)}
.shares{position:absolute;top:268px;left:278px;display:flex;gap:14px}
.share{display:flex;font-size:11.5px}
.share b{font-weight:600;color:#3b5a8a;border:1px solid #cdd2d9;background:#eef1f5;padding:2px 8px;border-radius:2px}
.share span{border:1px solid #cdd2d9;padding:2px 6px;margin-left:3px;color:var(--ink)}
.article-rule{position:absolute;top:320px;left:0;width:587px;height:1px;background:var(--line)}
.pager{left:99px;top:2384px;display:flex;gap:7px;font-size:12px}
.pager span{border:1px solid #d5d7da;height:24px;min-width:24px;padding:0 8px;display:flex;align-items:center;justify-content:center;color:var(--text)}
.pager .current{background:var(--orange);border-color:var(--orange);color:#fff}
.pager .wide{padding:0 14px}

/* sidebar */
.side{left:740px;width:361px}
.search-box{top:540px;height:130px;background:var(--blue);padding:19px 23px}
.search-box h3{font-size:16px;color:#fff;font-family:"Raleway",Arial,sans-serif;font-weight:700}
.search-row{margin-top:20px;display:flex;height:45px}
.search-row div{flex:1;background:#fff;font-size:11px;color:var(--text);display:flex;align-items:center;padding-left:14px}
.search-row span{width:52px;background:var(--orange);color:#fff;font-weight:700;font-size:13px;display:flex;align-items:center;justify-content:center}
.side-title{font-size:16.5px}
.blog-box{top:735px;height:199px;background:var(--panel);border:1px solid var(--line);padding:24px 18px}
.blog-input{height:44px;background:#fff;border:1px solid #dfe0e2;font-size:11px;display:flex;align-items:center;padding-left:18px;color:var(--text)}
.blog-btn{margin-top:12px;height:44px;background:var(--orange);color:#fff;font-family:"Raleway",Arial,sans-serif;font-weight:700;font-size:15px;display:flex;align-items:center;justify-content:center}
.blog-note{margin-top:14px;font-size:11.5px;line-height:20px;color:var(--text)}
.side-rule{height:1px;background:var(--line)}
.socials{top:1018px;display:flex;gap:14px}
.socials i{display:block;width:48px;height:48px;border-radius:50%}
.discussed{display:flex;gap:16px;height:80px}
.discussed .pic{width:110px;height:73px;flex:none;border:2px solid #fff;box-shadow:0 0 0 1px #d9dadc}
.discussed p{font-family:"Raleway",Arial,sans-serif;font-weight:700;font-size:13.5px;line-height:23px;color:var(--ink);text-decoration:underline;text-decoration-color:#c8cacd}
.discussed small{display:block;margin-top:10px;font-size:11.5px;color:var(--muted)}
.view-more{top:1458px;height:44px;border:1px solid #d5d7da;display:flex;align-items:center;justify-content:center;font-family:"Raleway",Arial,sans-serif;font-weight:700;font-size:14px;color:var(--ink)}
.community-card{top:1594px;height:269px;border:1px solid #dcdde0;background:var(--panel)}
.card-cover{height:150px;background:linear-gradient(135deg,#6d7a86,#a89c8c 55%,#5f6d7c)}
.card-avatar{position:absolute;left:18px;top:16px;width:66px;height:66px;border:2px solid #fff;background:#8a97a4}
.card-name{position:absolute;left:106px;top:22px;color:#fff;font-family:"Raleway",Arial,sans-serif;font-weight:700;font-size:14px}
.card-likes{position:absolute;left:106px;top:44px;color:#fff;font-size:11.5px;font-weight:600}
.card-btn{position:absolute;top:112px;height:27px;background:#f6f7f9;border:1px solid #ccd0d5;font-size:12.5px;font-weight:700;color:#4b4f56;display:flex;align-items:center;padding:0 10px}
.card-note{position:absolute;left:20px;top:168px;font-size:11px;color:var(--text)}
.card-faces{position:absolute;left:20px;top:196px;display:flex;gap:6px}
.card-faces i{display:block;width:48px;height:48px;background:#a9a29a}
.communities{top:1937px}
.communities li{list-style:none;height:44.8px;border-bottom:1px solid var(--line);display:flex;align-items:center;font-size:13px;color:var(--text)}
.side-more{right:99px;top:2402px;font-family:"Raleway",Arial,sans-serif;font-weight:700;font-size:12.5px;color:var(--orange)}

/* footer */
.footer{top:2468px;left:0;width:1200px;height:280px;background:var(--footer);border-top:5px solid var(--blue)}
.footer-brand{left:99px;top:2558px;font-family:"Raleway",Arial,sans-serif;font-weight:800;font-size:27px;color:#fff}
.f-title{font-family:"Raleway",Arial,sans-serif;font-weight:700;font-size:16px;color:#fff;text-transform:uppercase}
.f-links{list-style:none;margin-top:18px;font-size:12px;line-height:17px;color:var(--footer-text)}
.f-text{margin-top:16px;font-size:12px;line-height:20px;color:var(--footer-text)}
.f-input{margin-top:14px;width:255px;height:36px;background:#fff;font-size:11px;color:var(--muted);display:flex;align-items:center;padding-left:14px}
.f-btn{margin-top:16px;width:86px;height:32px;background:var(--orange);color:#fff;font-size:10.5px;font-weight:700;display:flex;align-items:center;justify-content:center}
.contact-list{list-style:none;margin-top:16px;font-size:12px;color:var(--footer-text)}
.contact-list li{display:flex;gap:14px;align-items:flex-start;line-height:24px;margin-bottom:6px}
.contact-list svg{width:13px;height:13px;margin-top:5px;flex:none}
.contact-list a{color:var(--footer-text)}
.copyright{left:99px;top:2712px;font-size:11.5px;color:var(--footer-text)}
.f-social{right:120px;top:2708px;display:flex;gap:10px}
.f-social i{display:block;width:18px;height:18px;background:#dfe1e4;border-radius:2px}
</style>
</head>
<body>
<div class="page">

  <!-- header -->
  <div class="abs top-rule"></div>
  <div class="abs brand">I LOVE BRAMBLE CREST</div>
  <div class="abs utility">Hot Topics<span>|</span>Newsletter Sign-Up<span>|</span>Support<span>|</span>Login<span>|</span>Register</div>
  <nav class="abs nav">
    <span class="active">HOME</span><span>ABOUT</span><span>ACADEMY</span><span>REFERENCE</span><span>SELLING</span><span>BUYING</span><span>BLOGGER</span><span>CONTACT</span>
    <svg width="14" height="14" viewBox="0 0 14 14"><circle cx="6" cy="6" r="4.3" fill="none" stroke="#1f2226" stroke-width="2"/><line x1="9.2" y1="9.2" x2="13" y2="13" stroke="#1f2226" stroke-width="2.2"/></svg>
  </nav>

  <!-- hero -->
  <div class="abs hero" role="img" aria-label="Town view with church spire, domed state house and a harbour with sailboats"></div>
  <div class="abs hero-shade"></div>
  <h1 class="abs hero-title">I LOVE BRAMBLE CREST</h1>
  <p class="abs hero-lead">Bramble Crest is a subdivision in Bethesda Maryland where I want to increase my listings of houses for sale. Bethesda Maryland is a Mayberry community but with a Global feel.</p>
  <div class="abs hero-btn">GET MORE INFO &gt;&gt;</div>
  <div class="abs hero-dots"><i></i><i></i><i></i><i></i></div>

  <!-- recent articles -->
  <h2 class="abs heading section-title">Recent Articles</h2>
  <div class="abs section-rule"></div>

  <article class="abs article" style="top:610px">
    <h3 class="article-title">Nemo enim ipsam voluptatem quia voluptas sit</h3>
    <div class="meta">
      <svg viewBox="0 0 11 11"><rect x="0.5" y="1.5" width="10" height="9" fill="none" stroke="#8d9196"/><rect x="0.5" y="1.5" width="10" height="3" fill="#8d9196"/></svg>May 6, 2015<span class="sep">|</span>
      <svg viewBox="0 0 11 11"><path d="M1 1h9v6H5l-3 3V7H1z" fill="#8d9196"/></svg>0 Comments<span class="sep">|</span>
      <svg viewBox="0 0 11 11"><path d="M2 9l5-5" stroke="#8d9196" stroke-width="2"/><circle cx="8" cy="3" r="2.2" fill="#8d9196"/></svg>in Resources, Tools &amp; Resources<span class="sep">|</span>
      <svg viewBox="0 0 11 11"><circle cx="5.5" cy="3" r="2.5" fill="#8d9196"/><path d="M1 11c0-4 9-4 9 0z" fill="#8d9196"/></svg>admin
    </div>
    <div class="progress"></div>
    <svg class="progress-marker" viewBox="0 0 16 18"><line x1="8" y1="0" x2="8" y2="8" stroke="#fff" stroke-width="2"/><path d="M2 17L8 8l6 9z" fill="#1f2226"/></svg>
    <div class="thumb" role="img" aria-label="Group of people standing in a circle seen from above" style="background:linear-gradient(135deg,#c9c3b8,#8c7b6a 45%,#d9b35a 70%,#6b7f96)"></div>
    <p class="excerpt">At vero eos et accusamus et iusto odio dignissimos ducimus qui blanditiis praesentium voluptatum del eniti atque corrupti quos dolores et quas molestias excepturi sint occaecati cupi..</p>
    <div class="read-more">READ MORE &gt;&gt;</div>
    <div class="shares"><div class="share"><b>Like</b><span>200</span></div><div class="share"><b>Tweet</b><span>200</span></div><div class="share"><b>+1</b><span>200</span></div></div>
    <div class="article-rule"></div>
  </article>

  <article class="abs article" style="top:964px">
    <h3 class="article-title">Nemo enim ipsam voluptatem quia voluptas sit</h3>
    <div class="meta">
      <svg viewBox="0 0 11 11"><rect x="0.5" y="1.5" width="10" height="9" fill="none" stroke="#8d9196"/><rect x="0.5" y="1.5" width="10" height="3" fill="#8d9196"/></svg>May 6, 2015<span class="sep">|</span>
      <svg viewBox="0 0 11 11"><path d="M1 1h9v6H5l-3 3V7H1z" fill="#8d9196"/></svg>0 Comments<span class="sep">|</span>
      <svg viewBox="0 0 11 11"><path d="M2 9l5-5" stroke="#8d9196" stroke-width="2"/><circle cx="8" cy="3" r="2.2" fill="#8d9196"/></svg>in Resources, Tools &amp; Resources<span class="sep">|</span>
      <svg viewBox="0 0 11 11"><circle cx="5.5" cy="3" r="2.5" fill="#8d9196"/><path d="M1 11c0-4 9-4 9 0z" fill="#8d9196"/></svg>admin
    </div>
    <div class="progress"></div>
    <svg class="progress-marker" viewBox="0 0 16 18"><line x1="8" y1="0" x2="8" y2="8" stroke="#fff" stroke-width="2"/><path d="M2 17L8 8l6 9z" fill="#1f2226"/></svg>
    <div class="thumb" role="img" aria-label="Smiling family of four lying together on a sofa" style="background:linear-gradient(135deg,#f1ede8,#d9b9a0 50%,#6f6a68)"></div>
    <p class="excerpt">At vero eos et accusamus et iusto odio dignissimos ducimus qui blanditiis praesentium voluptatum del eniti atque corrupti quos dolores et quas molestias excepturi sint occaecati cupi..</p>
    <div class="read-more">READ MORE &gt;&gt;</div>
    <div class="shares"><div class="share"><b>Like</b><span>200</span></div><div class="share"><b>Tweet</b><span>200</span></div><div class="share"><b>+1</b><span>200</span></div></div>
    <div class="article-rule"></div>
  </article>

  <article class="abs article" style="top:1318px">
    <h3 class="article-title">Nemo enim ipsam voluptatem quia voluptas sit</h3>
    <div class="meta">
      <svg viewBox="0 0 11 11"><rect x="0.5" y="1.5" width="10" height="9" fill="none" stroke="#8d9196"/><rect x="0.5" y="1.5" width="10" height="3" fill="#8d9196"/></svg>May 6, 2015<span class="sep">|</span>
      <svg viewBox="0 0 11 11"><path d="M1 1h9v6H5l-3 3V7H1z" fill="#8d9196"/></svg>0 Comments<span class="sep">|</span>
      <svg viewBox="0 0 11 11"><path d="M2 9l5-5" stroke="#8d9196" stroke-width="2"/><circle cx="8" cy="3" r="2.2" fill="#8d9196"/></svg>in Resources, Tools &amp; Resources<span class="sep">|</span>
      <svg viewBox="0 0 11 11"><circle cx="5.5" cy="3" r="2.5" fill="#8d9196"/><path d="M1 11c0-4 9-4 9 0z" fill="#8d9196"/></svg>admin
    </div>
    <div class="progress"></div>
    <svg class="progress-marker" viewBox="0 0 16 18"><line x1="8" y1="0" x2="8" y2="8" stroke="#fff" stroke-width="2"/><path d="M2 17L8 8l6 9z" fill="#1f2226"/></svg>
    <div class="thumb" role="img" aria-label="Soccer players competing for the ball on a grass pitch" style="background:linear-gradient(180deg,#3a4f8c 0%,#b8403e 45%,#4f8f3a 75%,#3f7a2f)"></div>
    <p class="excerpt">At vero eos et accusamus et iusto odio dignissimos ducimus qui blanditiis praesentium voluptatum del eniti atque corrupti quos dolores et quas molestias excepturi sint occaecati cupi..</p>
    <div class="read-more">READ MORE &gt;&gt;</div>
    <div class="shares"><div class="share"><b>Like</b><span>200</span></div><div class="share"><b>Tweet</b><span>200</span></div><div class="share"><b>+1</b><span>200</span></div></div>
    <div class="article-rule"></div>
  </article>

  <article class="abs article" style="top:1672px">
    <h3 class="article-title">Nemo enim ipsam voluptatem quia voluptas sit</h3>
    <div class="meta">
      <svg viewBox="0 0 11 11"><rect x="0.5" y="1.5" width="10" height="9" fill="none" stroke="#8d9196"/><rect x="0.5" y="1.5" width="10" height="3" fill="#8d9196"/></svg>May 6, 2015<span class="sep">|</span>
      <svg viewBox="0 0 11 11"><path d="M1 1h9v6H5l-3 3V7H1z" fill="#8d9196"/></svg>0 Comments<span class="sep">|</span>
      <svg viewBox="0 0 11 11"><path d="M2 9l5-5" stroke="#8d9196" stroke-width="2"/><circle cx="8" cy="3" r="2.2" fill="#8d9196"/></svg>in Resources, Tools &amp; Resources<span class="sep">|</span>
      <svg viewBox="0 0 11 11"><circle cx="5.5" cy="3" r="2.5" fill="#8d9196"/><path d="M1 11c0-4 9-4 9 0z" fill="#8d9196"/></svg>admin
    </div>
    <div class="progress"></div>
    <svg class="progress-marker" viewBox="0 0 16 18"><line x1="8" y1="0" x2="8" y2="8" stroke="#fff" stroke-width="2"/><path d="M2 17L8 8l6 9z" fill="#1f2226"/></svg>
    <div class="thumb" role="img" aria-label="Mountain bikers riding down a dusty trail" style="background:linear-gradient(135deg,#9aa3a8,#5b5f62 50%,#2c2e30)"></div>
    <p class="excerpt">At vero eos et accusamus et iusto odio dignissimos ducimus qui blanditiis praesentium voluptatum del eniti atque corrupti quos dolores et quas molestias excepturi sint occaecati cupi..</p>
    <div class="read-more">READ MORE &gt;&gt;</div>
    <div class="shares"><div class="share"><b>Like</b><span>200</span></div><div class="share"><b>Tweet</b><span>200</span></div><div class="share"><b>+1</b><span>200</span></div></div>
    <div class="article-rule"></div>
  </article>

  <article class="abs article" style="top:2026px">
    <h3 class="article-title">Nemo enim ipsam voluptatem quia voluptas sit</h3>
    <div class="meta">
      <svg viewBox="0 0 11 11"><rect x="0.5" y="1.5" width="10" height="9" fill="none" stroke="#8d9196"/><rect x="0.5" y="1.5" width="10" height="3" fill="#8d9196"/></svg>May 6, 2015<span class="sep">|</span>
      <svg viewBox="0 0 11 11"><path d="M1 1h9v6H5l-3 3V7H1z" fill="#8d9196"/></svg>0 Comments<span class="sep">|</span>
      <svg viewBox="0 0 11 11"><path d="M2 9l5-5" stroke="#8d9196" stroke-width="2"/><circle cx="8" cy="3" r="2.2" fill="#8d9196"/></svg>in Resources, Tools &amp; Resources<span class="sep">|</span>
      <svg viewBox="0 0 11 11"><circle cx="5.5" cy="3" r="2.5" fill="#8d9196"/><path d="M1 11c0-4 9-4 9 0z" fill="#8d9196"/></svg>admin
    </div>
    <div class="progress"></div>
    <svg class="progress-marker" viewBox="0 0 16 18"><line x1="8" y1="0" x2="8" y2="8" stroke="#fff" stroke-width="2"/><path d="M2 17L8 8l6 9z" fill="#1f2226"/></svg>
    <div class="thumb" role="img" aria-label="Farmers market stall with crates of apples and shoppers" style="background:linear-gradient(135deg,#8a7a6a,#c0502e 45%,#d98b2f 70%,#6a5a4a)"></div>
    <p class="excerpt">At vero eos et accusamus et iusto odio dignissimos ducimus qui blanditiis praesentium voluptatum del eniti atque corrupti quos dolores et quas molestias excepturi sint occaecati cupi..</p>
    <div class="read-more">READ MORE &gt;&gt;</div>
    <div class="shares"><div class="share"><b>Like</b><span>200</span></div><div class="share"><b>Tweet</b><span>200</span></div><div class="share"><b>+1</b><span>200</span></div></div>
    <div class="article-rule"></div>
  </article>

  <div class="abs pager">
    <span class="wide">Prev</span><span class="current">1</span><span>2</span><span>3</span><span>4</span><span>5</span><span>6</span><span>...</span><span>22</span><span class="wide">Next</span>
  </div>

  <!-- sidebar -->
  <div class="abs side search-box">
    <h3>START YOUR PROPERTY SEARCH</h3>
    <div class="search-row"><div>PROPERTY TYPE</div><span>GO</span></div>
  </div>

  <h3 class="abs side heading side-title" style="top:699px">Receive the Blog</h3>
  <div class="abs side blog-box">
    <div class="blog-input">ENTER YOUR EMAIL ADDRESS</div>
    <div class="blog-btn">SIGN UP</div>
    <p class="blog-note">By signing up, you are opting in to receive periodic communications from the Bramble Crest.</p>
  </div>
  <div class="abs side side-rule" style="top:961px"></div>

  <h3 class="abs side heading side-title" style="top:981px">Social Media</h3>
  <div class="abs side socials">
    <i style="background:#3b5a9a"></i><i style="background:#3fb0e8"></i><i style="background:#e0473a"></i><i style="background:#f0a458"></i><i style="background:#c8232c"></i><i style="background:#9b6a4c"></i>
  </div>
  <div class="abs side side-rule" style="top:1088px"></div>

  <h3 class="abs side heading side-title" style="top:1111px">Most Discussed</h3>
  <div class="abs side" style="top:1164px">
    <div class="discussed">
      <div class="pic" role="img" aria-label="Woman stretching outdoors in a park" style="background:linear-gradient(135deg,#e9d26a,#7aa04a)"></div>
      <div><p>Contrary to popular beliefgdgorem Ipsum is random texLatin</p><small>Feb 06, 2016 &nbsp;&nbsp;|&nbsp;&nbsp; 3</small></div>
    </div>
    <div class="discussed" style="margin-top:15px">
      <div class="pic" role="img" aria-label="Students seated in a classroom" style="background:linear-gradient(135deg,#c7b8a6,#8a6e5a)"></div>
      <div><p>Contrary to popular beliefgdgorem Ipsum is random texLatin</p><small>Feb 06, 2016 &nbsp;&nbsp;|&nbsp;&nbsp; 3</small></div>
    </div>
    <div class="discussed" style="margin-top:15px">
      <div class="pic" role="img" aria-label="People paddling kayaks on a lake" style="background:linear-gradient(135deg,#5d9fc4,#2f6e8f 60%,#d9643a)"></div>
      <div><p>Contrary to popular beliefgdgorem Ipsum is random texLatin</p><small>Feb 06, 2016 &nbsp;&nbsp;|&nbsp;&nbsp; 3</small></div>
    </div>
  </div>
  <div class="abs side view-more">VIEW MORE</div>

  <h3 class="abs side heading side-title" style="top:1549px">Join Me on Porchlight</h3>
  <div class="abs side community-card">
    <div class="card-cover" role="img" aria-label="Cover photo of a rocky mountain landscape"></div>
    <div class="card-avatar" role="img" aria-label="Profile photo of a hiker on a summit"></div>
    <div class="card-name">I LOVE BRAMBLE CREST</div>
    <div class="card-likes">4,893 LIKES</div>
    <div class="card-btn" style="left:18px">Like Page</div>
    <div class="card-btn" style="right:18px">Sign Up</div>
    <div class="card-note">Be the first of your friends to like this</div>
    <div class="card-faces" role="img" aria-label="Row of friend profile photos">
      <i></i><i style="background:#b8b2a8"></i><i></i><i style="background:#bfa392"></i><i style="background:#8f9aa3"></i><i style="background:#b3ab9f"></i>
    </div>
  </div>

  <h3 class="abs side heading side-title" style="top:1904px">Featured Communities</h3>
  <ul class="abs side communities">
    <li>OMT Sold Properties</li>
    <li>District of Columbia NW</li>
    <li>District of Columbia NE</li>
    <li>District of Columbia SW</li>
    <li>District of Columbia SE</li>
    <li>Maryland</li>
    <li>Virginia</li>
    <li>OMT Sold Properties</li>
    <li>District of Columbia NW</li>
    <li>District of Columbia NE</li>
  </ul>
  <div class="abs side-more">VIEW MORE &gt;&gt;</div>

  <!-- footer -->
  <footer class="abs footer"></footer>
  <div class="abs footer-brand">I LOVE BRAMBLE CREST</div>

  <div class="abs" style="left:427px;top:2502px">
    <h4 class="f-title">Information</h4>
    <ul class="f-links"><li>Home</li><li>About</li><li>Academy</li><li>Reference</li><li>Selling</li><li>Buying</li><li>Blogger</li><li>Contact</li></ul>
  </div>

  <div class="abs" style="left:595px;top:2502px">
    <h4 class="f-title">Newsletter Subscription</h4>
    <p class="f-text">Register Your Email Address to get<br>Information about us</p>
    <div class="f-input">Email Address</div>
    <div class="f-btn">SUBSCRIBE</div>
  </div>

  <div class="abs" style="left:910px;top:2502px">
    <h4 class="f-title">Contact Us</h4>
    <ul class="contact-list">
      <li><svg viewBox="0 0 13 13"><path d="M6.5 0C3.9 0 2 2 2 4.5 2 8 6.5 13 6.5 13S11 8 11 4.5C11 2 9.1 0 6.5 0z" fill="#fff"/><circle cx="6.5" cy="4.5" r="1.7" fill="#25272c"/></svg><span>12/4, Linden Row, Oakhaven<br>88, Quarry Lane, Fernley</span></li>
      <li><svg viewBox="0 0 13 13"><path d="M3 0l2 3-1.3 1.5c.8 1.8 2.3 3.3 4.1 4.1L9.3 7.3l3 2-1 3C6 13 0 7 .7 2z" fill="#fff"/></svg><span>1 555 010 2040</span></li>
      <li><svg viewBox="0 0 13 13"><rect x="2" y="0" width="9" height="4" fill="#fff"/><rect x="0" y="4" width="13" height="6" fill="#fff"/><rect x="3" y="8" width="7" height="5" fill="#fff" stroke="#25272c"/></svg><span>1 555 010 3090</span></li>
      <li><svg viewBox="0 0 13 13"><rect x="0" y="2" width="13" height="9" fill="#fff"/><path d="M0 2l6.5 5L13 2" fill="none" stroke="#25272c"/></svg><a>hello@bramblecrestliving.net</a></li>
    </ul>
  </div>

  <div class="abs copyright">© 2016, I Love Bramble Crest. All rights reserved.</div>
  <div class="abs f-social"><i></i><i></i><i></i></div>
</div>
</body>
</html>
```